Youtube Add for Online Bible School

I want a design for a Non-Video YouTube Add for my Online Bible School. I do not know the sizes that are needed nor the formats they need to be in so this is why I need you! I have a logo that should be used and an idea for the layout but I am free for suggestions.

```html
<!DOCTYPE html>
<html lang="en">
<head>
<meta charset="utf-8">
<title>Ridgeway Scripture Academy – Study Online in Nepali</title>
<link rel="stylesheet" href="https://fonts.googleapis.com/css2?family=Righteous&display=swap">
<style>
  :root {
    --sky-top: #b9d0e4;
    --sky-mid: #dce8f2;
    --snow: #f7fafd;
    --ridge-shade: #9fb4c8;
    --navy: #1d2f66;
    --button-blue: #1f4fb8;
    --button-edge: #0f2f7a;
    --white: #ffffff;
  }
  html, body {
    margin: 0;
    padding: 0;
    overflow: hidden;
  }
  .banner {
    position: relative;
    width: 1200px;
    height: 148px;
    overflow: hidden;
    background: var(--snow);
  }
  .scenery {
    position: absolute;
    inset: 0;
    background:
      linear-gradient(180deg, rgba(255,255,255,0) 55%, var(--snow) 100%),
      radial-gradient(ellipse 60% 70% at 15% 60%, rgba(255,255,255,0.95), rgba(255,255,255,0) 70%),
      linear-gradient(180deg, var(--sky-top) 0%, var(--sky-mid) 45%, var(--ridge-shade) 70%, var(--snow) 100%);
  }
  .brand {
    position: absolute;
    left: 70px;
    top: 56px;
    display: flex;
    align-items: center;
    gap: 12px;
  }
  .brand-square {
    width: 30px;
    height: 30px;
    background: var(--navy);
  }
  .brand-name {
    margin: 0;
    font-family: "Righteous", sans-serif;
    font-weight: 400;
    font-size: 22px;
    line-height: 1;
    color: var(--navy);
    white-space: nowrap;
  }
  .headline {
    position: absolute;
    left: 492px;
    top: 22px;
    margin: 0;
    font-family: "Righteous", sans-serif;
    font-weight: 400;
    font-size: 54px;
    line-height: 1;
    letter-spacing: 1px;
    color: var(--white);
    text-transform: uppercase;
    white-space: nowrap;
    text-shadow: 0 1px 3px rgba(40, 70, 110, 0.35);
  }
  .cta {
    position: absolute;
    left: 962px;
    top: 82px;
    width: 208px;
    height: 44px;
    border-radius: 7px;
    background: linear-gradient(180deg, #3a6fd6 0%, var(--button-blue) 55%, var(--button-edge) 100%);
    box-shadow: 0 2px 4px rgba(10, 30, 80, 0.45);
    display: flex;
    align-items: center;
    justify-content: center;
    font-family: "Righteous", sans-serif;
    font-size: 26px;
    letter-spacing: 1px;
    color: var(--white);
    text-decoration: none;
    text-transform: uppercase;
    box-sizing: border-box;
  }
</style>
</head>
<body>
  <div class="banner">
    <div class="scenery" role="img" aria-label="Photograph of snow-covered Himalayan mountain peaks under a pale winter sky"></div>

    <div class="brand">
      <div class="brand-square"></div>
      <p class="brand-name">Ridgeway Scripture Academy</p>
    </div>

    <h1 class="headline">Study Online in Nepali</h1>

    <a class="cta" href="#">Click Here</a>
  </div>
</body>
</html>
```